Property Management Company

We are looking for a sharp/modern business card design for a property management company.
We have included what should be on the business card down below in business card details.
Target Market(s)
Commercial properties, Home Owners
Industry/Entity Type
Business
Contact Information for Business Card
Name: Dale Orsino | Owner
Business Name : Kestrel Yards
Slogan : A Smarter Choice
Phone : 555.304.8862
Website: www.kestrelyards.example
E-Mail : dale@kestrelyards.example
Our Services are Commercial & Residential
-Asphalt Maintenance
-Snow Management
-Landscaping
-Blacktop
Free Estimates
Free parking lot cleanup & restripe with snow removal contract
Look and feel

```html
<!DOCTYPE html>
<html lang="en">
<head>
<meta charset="utf-8">
<title>Kestrel Yards – Business Card</title>
<link rel="stylesheet" href="https://fonts.googleapis.com/css2?family=Open+Sans:wght@400;600;700&family=Oswald:wght@500&display=swap">
<style>
  :root {
    --backdrop: #e9e6e1;
    --card: #ffffff;
    --red: #c8202f;
    --navy: #1f2a5c;
    --green: #1f8a3b;
    --faint: #eceef3;
  }
  * { box-sizing: border-box; margin: 0; padding: 0; }
  html, body { width: 1200px; height: 784px; overflow: hidden; }
  body {
    background: var(--backdrop);
    font-family: "Open Sans", Arial, sans-serif;
    position: relative;
  }
  .card {
    position: absolute;
    top: 232px;
    width: 560px;
    height: 320px;
    background: var(--card);
    box-shadow: 0 4px 14px rgba(0,0,0,.12);
    overflow: hidden;
  }
  .card--back { left: 27px; }
  .card--front { left: 613px; }

  /* back */
  .back-accent {
    position: absolute;
    left: 40px; top: 50px;
    width: 480px; height: 170px;
    background: linear-gradient(90deg, var(--faint), #f6efec);
  }
  .services {
    position: relative;
    list-style: none;
    text-align: center;
    padding-top: 40px;
    font-family: "Oswald", "Arial Narrow", sans-serif;
    font-weight: 500;
    text-transform: uppercase;
    letter-spacing: 1.6px;
    font-size: 15px;
    line-height: 38px;
  }
  .services .red { color: var(--red); }
  .services .navy { color: var(--navy); }
  .promo {
    position: absolute;
    left: 0; right: 0; bottom: 42px;
    text-align: center;
    font-family: "Oswald", "Arial Narrow", sans-serif;
    font-weight: 500;
    text-transform: uppercase;
    letter-spacing: 1.6px;
    font-size: 15px;
    color: var(--navy);
  }

  /* front */
  .swoosh { position: absolute; inset: 0; }
  .brand {
    position: absolute;
    left: 0; right: 0; top: 62px;
    text-align: center;
  }
  .brand-name {
    display: inline-flex;
    align-items: center;
    gap: 12px;
    font-weight: 700;
    font-size: 38px;
    color: var(--navy);
  }
  .brand-mark {
    width: 22px; height: 22px;
    background: var(--red);
  }
  .brand-line {
    margin-top: 4px;
    font-weight: 600;
    font-size: 16px;
    color: var(--green);
  }
  .person {
    position: absolute;
    left: 90px; top: 232px;
    text-align: right;
  }
  .person-name { font-size: 24px; font-weight: 700; color: var(--red); }
  .person-role { font-size: 16px; color: var(--navy); margin-top: -2px; }
  .contact {
    position: absolute;
    left: 320px; top: 204px;
    list-style: none;
    font-size: 15px;
    color: var(--navy);
    line-height: 22px;
  }
  .contact li { display: flex; align-items: center; gap: 8px; }
  .contact svg { width: 14px; height: 14px; fill: var(--red); flex: none; }
</style>
</head>
<body>

<section class="card card--back">
  <div class="back-accent" role="img" aria-label="Faint brand backdrop"></div>
  <ul class="services">
    <li class="red">Commercial &amp; Residential</li>
    <li class="navy">Asphalt Maintenance</li>
    <li class="red">Snow Management</li>
    <li class="navy">Landscaping</li>
    <li class="red">Blacktop Free Estimates</li>
  </ul>
  <p class="promo">Free parking lot cleanup &amp; restripe with snow removal contract</p>
</section>

<section class="card card--front">
  <svg class="swoosh" viewBox="0 0 560 320" preserveAspectRatio="none" aria-hidden="true">
    <polygon points="560,98 560,120 345,190" fill="var(--red)"/>
    <polygon points="0,228 0,254 300,212" fill="var(--red)"/>
  </svg>
  <div class="brand">
    <div class="brand-name"><span class="brand-mark"></span>Kestrel Yards</div>
    <div class="brand-line">Asphalt &amp; Snow Removal</div>
  </div>
  <div class="person">
    <div class="person-name">Dale Orsino</div>
    <div class="person-role">Owner</div>
  </div>
  <ul class="contact">
    <li><svg viewBox="0 0 24 24"><path d="M6.6 10.8a15 15 0 0 0 6.6 6.6l2.2-2.2a1 1 0 0 1 1-.25 11.4 11.4 0 0 0 3.6.57 1 1 0 0 1 1 1V20a1 1 0 0 1-1 1A17 17 0 0 1 3 4a1 1 0 0 1 1-1h3.5a1 1 0 0 1 1 1c0 1.25.2 2.45.57 3.57a1 1 0 0 1-.25 1z"/></svg>555.304.8862</li>
    <li><svg viewBox="0 0 24 24"><path d="M2 5h20v14H2zm2 2v.5l8 5 8-5V7z"/></svg>dale@kestrelyards.example</li>
    <li><svg viewBox="0 0 24 24"><path d="M12 2a10 10 0 1 0 0 20 10 10 0 0 0 0-20zm-1 2.1V8H7.3A8 8 0 0 1 11 4.1zM13 4.1A8 8 0 0 1 16.7 8H13zM4.5 10H11v4H4.5a8 8 0 0 1 0-4zm8.5 0h6.5a8 8 0 0 1 0 4H13zM7.3 16H11v3.9A8 8 0 0 1 7.3 16zm5.7 0h3.7A8 8 0 0 1 13 19.9z"/></svg>www.kestrelyards.example</li>
  </ul>
</section>

</body>
</html>
```